Construction Company Business Card

Business Card Design using new Logo

Contact Information for Business Card

include all company info and website

Requirements
Must have
• Marlon Ridgeway - President
ph. 555-716-5093
Ashgrove Springs, ST
marlon@stonefieldworks.com
www.stonefieldworks.com

```html
<!DOCTYPE html>
<html lang="en">
<head>
<meta charset="UTF-8">
<title>Stonefield Works – Business Card</title>
<link rel="stylesheet" href="https://fonts.googleapis.com/css2?family=Montserrat:wght@400;500;600;700&display=swap">
<style>
  :root {
    --brand-red: #c8202a;
    --ink-grey: #4a4a4a;
    --soft-grey: #a3a3a6;
    --stripe-grey: #c3c3c7;
    --card-white: #ffffff;
    --page-bg: #e9e9eb;
  }
  * { box-sizing: border-box; margin: 0; padding: 0; }
  html, body { width: 1200px; height: 881px; overflow: hidden; }
  body {
    background: var(--page-bg);
    font-family: "Montserrat", sans-serif;
    position: relative;
  }
  .card {
    position: absolute;
    width: 560px;
    height: 320px;
    border-radius: 18px;
    overflow: hidden;
    left: 320px;
    box-shadow: 0 8px 24px rgba(0,0,0,0.12);
  }
  .card--front { top: 70px; background: var(--brand-red); }
  .card--back  { top: 470px; background: var(--card-white); }

  .front__decor {
    position: absolute;
    left: 60px; top: 30px;
    width: 440px; height: 260px;
    border-radius: 40px;
    background: radial-gradient(ellipse at center, rgba(255,255,255,0.10), rgba(255,255,255,0.02) 70%);
  }
  .front__logo {
    position: absolute;
    left: 0; right: 0; top: 128px;
    text-align: center;
    color: #fff;
    font-weight: 600;
    font-size: 30px;
    letter-spacing: 4px;
  }
  .front__rule {
    position: absolute;
    left: 150px; right: 150px; top: 176px;
    height: 1px; background: #fff;
  }

  .back__logo {
    position: absolute;
    left: 34px; top: 46px;
    display: flex; align-items: center; gap: 10px;
  }
  .back__logo-dot { width: 12px; height: 12px; border-radius: 50%; background: var(--brand-red); }
  .back__logo-name {
    color: var(--soft-grey);
    font-weight: 600;
    font-size: 18px;
    letter-spacing: 3px;
  }
  .back__tab {
    position: absolute; right: 0; top: 72px;
    width: 9px; height: 42px; background: var(--brand-red);
  }
  .person { position: absolute; right: 30px; top: 84px; text-align: right; }
  .person__name {
    color: var(--brand-red);
    font-weight: 700; font-size: 25px; letter-spacing: 1.5px;
    text-transform: uppercase; line-height: 1;
  }
  .person__title {
    color: var(--ink-grey);
    font-size: 15px; font-weight: 500; letter-spacing: 1px;
    margin-top: 6px;
  }
  .back__rule {
    position: absolute; left: 56px; right: 20px; top: 150px;
    height: 1px; background: var(--brand-red);
  }
  .location {
    position: absolute; right: 30px; top: 170px;
    display: flex; align-items: center; gap: 6px;
    color: var(--ink-grey); font-size: 14px; letter-spacing: 1px;
  }
  .contacts {
    position: absolute; left: 40px; top: 192px;
    list-style: none;
  }
  .contacts li {
    display: flex; align-items: center; gap: 9px;
    color: var(--ink-grey); font-size: 16px; letter-spacing: 0.8px;
    line-height: 25px;
  }
  .contacts svg { flex: none; }
  .back__wave { position: absolute; left: 0; bottom: 0; }
</style>
</head>
<body>

<section class="card card--front">
  <div class="front__decor" role="img" aria-label="Faint outline map decoration"></div>
  <div class="front__logo">STONEFIELD WORKS</div>
  <div class="front__rule"></div>
</section>

<section class="card card--back">
  <div class="back__logo">
    <span class="back__logo-dot"></span>
    <span class="back__logo-name">STONEFIELD WORKS</span>
  </div>
  <div class="back__tab"></div>

  <div class="person">
    <div class="person__name">Marlon Ridgeway</div>
    <div class="person__title">President</div>
  </div>

  <div class="back__rule"></div>

  <div class="location">
    <span>Ashgrove Springs, ST</span>
    <svg width="11" height="15" viewBox="0 0 12 16"><path d="M6 0C2.7 0 0 2.6 0 5.9 0 10.3 6 16 6 16s6-5.7 6-10.1C12 2.6 9.3 0 6 0zm0 8.2a2.3 2.3 0 1 1 0-4.6 2.3 2.3 0 0 1 0 4.6z" fill="var(--brand-red)"/></svg>
  </div>

  <ul class="contacts">
    <li>
      <svg width="12" height="14" viewBox="0 0 12 14"><path d="M3 1l2 3-1.3 1.3c.6 1.6 1.8 3 3.3 3.9L8.3 8l3 2-1.3 2.8C5 12.5 1 7.5.8 2.3z" fill="var(--brand-red)"/></svg>
      <span>555-716-5093</span>
    </li>
    <li>
      <svg width="14" height="11" viewBox="0 0 14 11"><rect x="0.7" y="0.7" width="12.6" height="9.6" fill="none" stroke="var(--brand-red)" stroke-width="1.4"/><path d="M1 1l6 5 6-5" fill="none" stroke="var(--brand-red)" stroke-width="1.4"/></svg>
      <span>marlon@stonefieldworks.com</span>
    </li>
    <li>
      <svg width="14" height="14" viewBox="0 0 14 14"><g fill="none" stroke="var(--brand-red)" stroke-width="1.2"><circle cx="7" cy="7" r="6"/><ellipse cx="7" cy="7" rx="2.6" ry="6"/><path d="M1 7h12M2 4h10M2 10h10"/></g></svg>
      <span>www.stonefieldworks.com</span>
    </li>
  </ul>

  <svg class="back__wave" width="560" height="120" viewBox="0 0 560 120">
    <path d="M0 104 L350 98 C380 97 392 90 400 80 L400 120 L0 120 Z" fill="var(--stripe-grey)"/>
    <path d="M0 110 L360 104 C395 103 405 88 425 62 C440 44 470 40 560 38 L560 120 L0 120 Z" fill="var(--brand-red)"/>
  </svg>
</section>

</body>
</html>
```